Harborvale Ventures brochure for Investment partnership, young harold pembly

We need a brochure design to attract new investors for our investing partnership Called Harborvale Ventures. We are based in New Orleans, La. We primarily invest in stocks, bonds, and crypto but venture out into other categories as well. We would like to see designs with the black and gold like our logo. The final design should say new, fresh, sleek, tech, and honorable. BROUCHURE WILL BE 4 pages.or one folded sheet a paparer if that makes sense.
Updates

A chart showing Harborvale Ventures gains since 2019 28.6 percent and the TR 400 gAINS 7.1 PERCENT

Target Market(s)

Probable Investors

Industry/Entity Type

Financial Planning

Colors

Designer to choose only greyscale colors for use in the design.

Requirements
Must have
• Black and Gold accent. Stock market feel. Sleek, High tech, innovative, Intellgent design.
Nice to have
• Page colors possibly black.
Should not have
• Boring, Old school,

```html
<!DOCTYPE html>
<html lang="en">
<head>
<meta charset="utf-8">
<title>Harborvale Ventures Brochure</title>
<link href="https://fonts.googleapis.com/css2?family=Poppins:wght@300;400;500&display=swap" rel="stylesheet">
<style>
  :root {
    --backdrop: #d4d4d9;
    --page: #0d0d0e;
    --page-edge: #1a1a1c;
    --gold: #cfa93c;
    --gold-light: #f3dc78;
    --gold-dark: #7a5a18;
    --text: #d9d9d9;
    --divider: #555555;
    --step-number: #2a2a2c;
  }
  * { margin: 0; padding: 0; box-sizing: border-box; }
  html, body {
    width: 1200px; height: 2346px; overflow: hidden;
    background: var(--backdrop);
    font-family: "Poppins", sans-serif;
  }
  .canvas { position: relative; width: 1200px; height: 2346px; }

  .page {
    position: absolute; overflow: hidden;
    background: radial-gradient(ellipse at 60% 40%, var(--page-edge), var(--page) 70%);
    box-shadow: 0 14px 30px rgba(0,0,0,.35);
  }
  .page svg.art { position: absolute; inset: 0; width: 100%; height: 100%; }
  .layer { position: absolute; left: 0; right: 0; text-align: center; }

  .brand {
    color: var(--gold); font-weight: 500; text-transform: uppercase;
    line-height: 1.1; letter-spacing: .08em;
  }
  .brand .brand-sub { display: block; letter-spacing: .35em; font-size: .5em; margin-top: 6px; }

  .gold-head { color: var(--gold); font-weight: 400; text-transform: uppercase; }
  .light-head { color: var(--text); font-weight: 300; text-transform: uppercase; }
  .rule { width: 96px; height: 2px; background: var(--gold); margin: 0 auto; }
  .body-copy { color: var(--text); font-weight: 300; font-size: 12.5px; line-height: 1.3; }

  /* cover */
  .cover { left: 50px; top: 403px; width: 540px; height: 700px; }
  .cover .brand { top: 200px; font-size: 52px; }
  .cover .tagline { top: 370px; font-size: 20px; line-height: 1.3; }
  .cover .club { top: 555px; font-size: 25px; line-height: 1.35; }

  /* back */
  .back { left: 610px; top: 403px; width: 540px; height: 700px; }
  .back .about { top: 240px; font-size: 21px; line-height: 1.4; }
  .back .rule { position: absolute; top: 328px; left: 222px; }
  .back .body-copy { top: 358px; padding: 0 78px; }
  .back .brand { top: 540px; font-size: 21px; }
  .contact {
    position: absolute; top: 622px; left: 52px; right: 56px;
    display: flex; font-size: 9px; color: var(--text); line-height: 1.4;
    white-space: nowrap;
  }
  .contact .col { flex: none; padding-right: 14px; margin-right: 14px; border-right: 1px solid var(--divider); }
  .contact .col:last-child { border: 0; margin-right: 0; padding-right: 0; }
  .contact .name { color: var(--gold); font-weight: 500; }
  .contact .key { color: var(--gold); }

  /* inside spread */
  .spread { left: 30px; top: 1183px; width: 1140px; height: 740px; }
  .spread .intro { top: 595px; left: 0; right: auto; width: 570px; padding: 0 55px; font-size: 13.5px; }
  .spread .brand { left: 570px; top: 55px; font-size: 38px; }
  .spread .works { left: 570px; top: 180px; font-size: 36px; letter-spacing: .02em; }
  .spread .rule { position: absolute; top: 240px; left: 805px; width: 100px; }
  .steps { position: absolute; left: 620px; top: 310px; width: 480px; list-style: none; }
  .step { display: flex; gap: 28px; margin-bottom: 26px; }
  .step-number { width: 40px; font-size: 60px; font-weight: 500; color: var(--step-number); line-height: .9; text-align: center; }
  .step .body-copy { font-size: 13.5px; line-height: 1.25; flex: 1; }
  .site { position: absolute; left: 570px; right: 0; top: 698px; text-align: center; color: var(--gold); font-size: 11px; letter-spacing: .5em; }
</style>
</head>
<body>
<div class="canvas">

  <section class="page cover">
    <svg class="art" viewBox="0 0 540 700" preserveAspectRatio="none">
      <defs>
        <linearGradient id="goldCover" x1="0" y1="1" x2="1" y2="0">
          <stop offset="0" stop-color="var(--gold-dark)"/>
          <stop offset=".6" stop-color="var(--gold)"/>
          <stop offset="1" stop-color="var(--gold-light)"/>
        </linearGradient>
      </defs>
      <path d="M0,112 C30,90 52,45 62,0 L58,0 C46,42 26,82 0,104 Z" fill="url(#goldCover)"/>
      <path d="M0,585 C90,520 200,515 320,510 C440,505 510,460 540,400 L540,450 C500,500 420,518 320,522 C200,527 80,540 0,600 Z" fill="url(#goldCover)"/>
      <path d="M0,600 C80,540 200,527 320,522 C420,518 500,500 540,450 L540,700 L0,700 Z" fill="#070707"/>
    </svg>
    <div class="layer brand">Harborvale<span class="brand-sub">Ventures</span></div>
    <p class="layer light-head tagline">Become a partner &amp; build<br>generational wealth by<br>investing in the stock market</p>
    <h2 class="layer gold-head club">A first of its kind<br>investment club</h2>
  </section>

  <section class="page back">
    <svg class="art" viewBox="0 0 540 700" preserveAspectRatio="none">
      <defs>
        <linearGradient id="goldBack" x1="0" y1="1" x2="1" y2="0">
          <stop offset="0" stop-color="var(--gold-light)"/>
          <stop offset=".45" stop-color="var(--gold)"/>
          <stop offset="1" stop-color="var(--gold-dark)"/>
        </linearGradient>
        <linearGradient id="streetTone" x1="0" y1="0" x2="0" y2="1">
          <stop offset="0" stop-color="#3a3a3b"/>
          <stop offset="1" stop-color="#1c1c1d"/>
        </linearGradient>
      </defs>
      <rect x="0" y="0" width="540" height="290" fill="url(#streetTone)" role="img" aria-label="Faded black and white photo of a city street with a streetcar"/>
      <path d="M0,270 C60,190 160,172 270,172 C400,172 500,150 540,110 L540,700 L0,700 Z" fill="#0d0d0e"/>
      <path d="M0,278 C40,200 150,172 270,170 C400,168 500,150 540,110 L540,118 C500,165 400,180 270,182 C160,184 60,210 0,290 Z" fill="url(#goldBack)"/>
      <path d="M490,700 C500,650 520,615 540,596 L540,602 C522,620 506,655 498,700 Z" fill="url(#goldBack)"/>
    </svg>
    <h2 class="layer gold-head about">About Harborvale Ventures<br>and general partner</h2>
    <div class="rule"></div>
    <p class="layer body-copy">Harborvale Ventures was founded in 2019 by General Partner Marcus Delaune with a group economic empowerment mission. Marcus Delaune has invested in stocks since a teenager, received his BA in economics from Bayou State University and is currently attending Gulf Coast University.</p>
    <div class="layer brand">Harborvale<span class="brand-sub">Ventures</span></div>
    <div class="contact">
      <div class="col"><span class="name">Harborvale Ventures</span><br>P.O. Box 4410, 210 Magazine St<br>New Orleans, LA</div>
      <div class="col"><span class="key">P :</span> +1 504 555 0182<br><span class="key">P :</span> +1 504 555 0183</div>
      <div class="col"><span class="key">E :</span> info@harborvale.example<br><span class="key">W :</span> www.harborvale.example</div>
    </div>
  </section>

  <section class="page spread">
    <svg class="art" viewBox="0 0 1140 740" preserveAspectRatio="none">
      <defs>
        <linearGradient id="goldSpread" x1="0" y1="0" x2="1" y2="0">
          <stop offset="0" stop-color="var(--gold-dark)"/>
          <stop offset=".5" stop-color="var(--gold-light)"/>
          <stop offset="1" stop-color="var(--gold)"/>
        </linearGradient>
        <linearGradient id="alleyTone" x1="0" y1="0" x2="0" y2="1">
          <stop offset="0" stop-color="#6a6a6c"/>
          <stop offset=".5" stop-color="#3c3c3e"/>
          <stop offset="1" stop-color="#1e1e1f"/>
        </linearGradient>
      </defs>
      <rect x="0" y="0" width="570" height="560" fill="url(#alleyTone)" role="img" aria-label="Black and white photo of a cathedral beside a narrow cobblestone alley"/>
      <path d="M0,512 C80,480 180,470 300,500 C420,535 520,500 570,440 L570,740 L0,740 Z" fill="#0d0d0e"/>
      <path d="M0,500 C80,470 180,462 300,490 C420,522 520,492 570,430 L570,442 C520,505 420,540 300,506 C180,474 80,482 0,518 Z" fill="url(#goldSpread)"/>
    </svg>
    <p class="layer body-copy intro">If you are receiving this brochure its because someone sees you as a person that doesn't want to just work and pay bills. Your someone who wants to build real generational wealth. Not throw schemes but the using the greatest wealth builder available. The stock market.</p>
    <div class="layer brand">Harborvale<span class="brand-sub">Ventures</span></div>
    <h2 class="layer gold-head works">How it works</h2>
    <div class="rule"></div>
    <ol class="steps">
      <li class="step"><span class="step-number">1</span><p class="body-copy">Make initial deposit. The general partner will invest in stocks, bonds and other investment vehicles on your behalf.</p></li>
      <li class="step"><span class="step-number">2</span><p class="body-copy">There is no upfront fees. The general partner will guarantee a 5 percent return and will work for free on your behalf until that is achieved. After the 5 percent return on the dollars invested the limited partner will receive 80 percent and the general partner will receive 20 percent of every dollar gained</p></li>
      <li class="step"><span class="step-number">3</span><p class="body-copy">As the return and investments multiply the interests begins to compound annually. The legal partner legally owns shares of stock within the club and may redeem once a year or let money continue to earn interest.</p></li>
    </ol>
    <div class="site">www.harborvale.example</div>
  </section>

</div>
</body>
</html>
```